Business card design and logo needed - Photographer

I take photos of weddings, rodeos, snowmobiling.
Need a card to hand out to prospective clients.
Industry/Entity Type
Business
Contact Information for Business Card
Marlon Pettibrook Photography
Requirements
Must have
- Bold
Black or white base.
My website. www.MarlonPettibrook.com
Should not have
- camera/ lens/ aperture blades

```html
<!DOCTYPE html>
<html lang="en">
<head>
<meta charset="utf-8">
<title>Marlon Pettibrook Photography – Business Card</title>
<link rel="stylesheet" href="https://fonts.googleapis.com/css2?family=Saira+Semi+Condensed:wght@400;500;600&display=swap">
<style>
  :root {
    --card-bg: #1a1f1f;
    --accent: #2ecbab;
    --text: #ffffff;
  }
  html, body {
    margin: 0;
    padding: 0;
    width: 1200px;
    height: 693px;
    overflow: hidden;
    background: var(--card-bg);
  }
  .card {
    position: relative;
    width: 1200px;
    height: 693px;
    background: var(--card-bg);
    overflow: hidden;
    font-family: "Saira Semi Condensed", "Arial Narrow", sans-serif;
    color: var(--text);
  }
  .brand-mark {
    position: absolute;
    left: 400px;
    top: 170px;
    width: 96px;
    height: 96px;
    background: var(--accent);
  }
  .brand-name {
    position: absolute;
    left: 514px;
    top: 92px;
    margin: 0;
    font-size: 92px;
    line-height: 100px;
    font-weight: 600;
    letter-spacing: 1px;
    color: var(--text);
  }
  .brand-name span { display: block; }
  .brand-tagline {
    position: absolute;
    left: 582px;
    top: 292px;
    margin: 0;
    font-size: 44px;
    line-height: 1;
    font-weight: 500;
  }
  .brand-website {
    position: absolute;
    left: 582px;
    top: 352px;
    margin: 0;
    font-size: 28px;
    line-height: 1;
    font-weight: 500;
    letter-spacing: 0.5px;
    color: var(--accent);
  }
  .contact {
    position: absolute;
    top: 514px;
    display: flex;
    align-items: center;
    gap: 18px;
    font-size: 31px;
    font-weight: 500;
    letter-spacing: 0.5px;
    white-space: nowrap;
  }
  .contact-email { left: 26px; }
  .contact-phone { left: 918px; }
  .contact-icon { width: 56px; height: 56px; flex: none; }
  .accent-band {
    position: absolute;
    left: 0;
    top: 0;
    width: 1200px;
    height: 693px;
  }
</style>
</head>
<body>
  <div class="card">
    <div class="brand-mark"></div>
    <h1 class="brand-name"><span>Marlon</span><span>Pettibrook</span></h1>
    <p class="brand-tagline">photography</p>
    <p class="brand-website">www.MarlonPettibrook.com</p>

    <div class="contact contact-email">
      <svg class="contact-icon" viewBox="0 0 56 56" aria-hidden="true">
        <circle cx="28" cy="28" r="25.5" fill="none" stroke="var(--accent)" stroke-width="3"/>
        <rect x="13" y="18" width="30" height="21" fill="none" stroke="var(--accent)" stroke-width="2"/>
        <polyline points="13,18 28,31 43,18" fill="none" stroke="var(--accent)" stroke-width="2"/>
        <line x1="13" y1="39" x2="24" y2="28" stroke="var(--accent)" stroke-width="2"/>
        <line x1="32" y1="28" x2="43" y2="39" stroke="var(--accent)" stroke-width="2"/>
      </svg>
      <span>hello@marlonpettibrook.com</span>
    </div>

    <div class="contact contact-phone">
      <svg class="contact-icon" viewBox="0 0 56 56" aria-hidden="true">
        <circle cx="28" cy="28" r="25.5" fill="none" stroke="var(--accent)" stroke-width="3"/>
        <path d="M19 15 l5 -2 l5 9 l-4 3 c1 4 4 8 8 11 l4 -3 l7 7 l-3 4 c-10 0 -22 -14 -22 -29 z" fill="var(--accent)"/>
      </svg>
      <span>306 555 0148</span>
    </div>

    <svg class="accent-band" viewBox="0 0 1200 693" aria-hidden="true">
      <polygon points="0,584 211,648 1200,589 1200,619 211,659 0,615" fill="var(--accent)"/>
    </svg>
  </div>
</body>
</html>
```